Revamp Current Website From 2012 TO 2018

We need a ravamp to our current website. I prefer a professional corporate modern feel to it.

My Current Website is www.brightlanepromoworks.biz. Please redesign the homepage and the /certs page first....see attached document for specific instructions..

There is a lot of content at the bottom but maybe we can shorten that by using titles and a pop up of the details or something so it doesnt take too mcuh space...or maybe a red more hyperlink to see the rest of info in pop up or something or new page...

Target Market(s)

B2B, business owners, website owners, marketing companies.

Industry/Entity Type

Promotional Product

Number of Pages Required

2 page

Colors

Designer to choose colors to be used in the design.

Requirements
Must have
• Please keep in mind logo mock up I am working on that looks beautiful on dark background for header...see attached for logo
• Must use existing content I hope your marketing mind comes in to play when designing the website.
• Must have all my content provided on each page...
Nice to have
• similiar color scheme...
Should not have
• I dont like using templates because usually hard to expand on design in future so Prefer full custom designs
• Please no templates

```html
<!DOCTYPE html>
<html lang="en">
<head>
<meta charset="utf-8">
<title>Brightlane Promo Works – Home</title>
<link rel="stylesheet" href="https://fonts.googleapis.com/css2?family=Open+Sans:wght@400;600;700;800&family=Oswald:wght@500;600&display=swap">
<style>
:root{
  --page:#2f3032;
  --topbar:#1d1e20;
  --nav:#26272a;
  --card:#e9e9e9;
  --card-inner:#f4f4f4;
  --blue:#1a78cf;
  --blue-bright:#2a8fe6;
  --ink:#333;
  --ink-soft:#555;
  --tile:#2b2c2e;
  --tile-bar:#48494c;
  --white:#fff;
  --hero-a:#3a2140;
  --hero-b:#8e6b92;
  --photo-a:#c9ccd0;
  --photo-b:#8f9498;
}
*{box-sizing:border-box;margin:0;padding:0}
html,body{width:1200px;height:5187px;overflow:hidden}
body{background:var(--page);font-family:"Open Sans",Arial,sans-serif;color:var(--ink);font-size:13px;line-height:1.5;position:relative}
.abs{position:absolute}
.topbar{top:0;left:0;width:1200px;height:28px;background:var(--topbar);color:#bbb;font-size:11px;display:flex;align-items:center;padding:0 18px;gap:24px}
.topbar .login{margin-left:auto;display:flex;gap:6px}
.topbar .field{width:110px;height:16px;background:#fff;border-radius:2px}
.topbar .btn{background:#555;color:#fff;padding:0 8px;height:16px;font-size:10px;border-radius:2px;line-height:16px}
.nav{top:28px;left:0;width:1200px;height:36px;background:var(--nav);display:flex;align-items:center;padding:0 18px}
.brand{display:flex;align-items:center;gap:8px;color:var(--white);font-weight:700;font-size:14px}
.brand i{width:14px;height:14px;background:var(--blue);display:block}
.nav ul{list-style:none;display:flex;margin-left:auto;margin-right:200px;gap:2px}
.nav li{color:#ccc;font-size:11px;padding:0 14px;line-height:36px}
.nav li.on{background:#3a3b3e;color:#fff}
.hero{top:64px;left:0;width:1200px;height:456px;background:linear-gradient(100deg,#202124 0%,var(--hero-a) 45%,var(--hero-b) 100%)}
.hero-title{top:115px;left:42px;color:#fff;font-family:"Oswald",sans-serif;font-weight:600;font-size:36px;line-height:1.15;text-transform:uppercase}
.hero-facts{top:225px;left:42px;color:#fff;font-size:14px;line-height:1.35}
.hero-cta{top:298px;left:895px;background:var(--blue);color:#fff;font-weight:700;font-size:17px;padding:16px 26px;display:flex;align-items:center;gap:12px}
.hero-cta b{width:26px;height:26px;border-radius:50%;background:#fff;color:var(--blue);display:flex;align-items:center;justify-content:center;font-size:14px}
.card{left:52px;width:1096px;background:var(--card)}
.h2{font-family:"Oswald",sans-serif;font-weight:600;text-transform:uppercase;color:var(--blue);font-size:40px;line-height:1.1}
.incentives{top:595px;height:252px;background:var(--blue);color:#fff;padding:24px 30px}
.incentives .h2{color:#fff}
.inc-cols{display:flex;gap:20px;margin-top:26px;font-size:13px;line-height:1.45}
.inc-cols ul{list-style:none;flex:1}
.feature{top:882px;height:259px;display:flex;padding:14px}
.photo{background:linear-gradient(135deg,var(--photo-a),var(--photo-b))}
.purple{background:linear-gradient(135deg,#5a3a5e,#b897b8 60%,#e3d2e0)}
.feature .photo{width:420px;height:231px}
.feature .txt{flex:1;padding:4px 8px 0 32px}
.sub{color:var(--blue);font-weight:800;text-transform:uppercase;font-size:15px;line-height:1.3}
.feature p{margin-top:12px;font-size:13px}
.plug{top:1176px;height:484px;padding:26px 30px}
.plug-grid{display:grid;grid-template-columns:1fr 1fr;gap:30px 40px;margin:34px 0 0 20px}
.plug-item{display:flex;gap:22px}
.icon-sq{width:100px;height:100px;background:#c7c7c7;flex:none;display:flex;align-items:center;justify-content:center}
.plug-item h3{font-size:14px;font-weight:700;color:#222}
.plug-item p{font-size:12.5px;margin-top:8px;line-height:1.45}
.dist{top:1694px;height:1124px;padding:26px 30px}
.dist-grid{display:grid;grid-template-columns:1fr 1fr;gap:30px 36px;margin-top:28px}
.tile-ico{height:172px;background:var(--tile);display:flex;align-items:center;justify-content:center}
.tile-bar{height:62px;background:var(--tile-bar);color:var(--blue-bright);font-size:26px;font-weight:600;display:flex;align-items:center;justify-content:center}
.tile p{font-size:13px;padding:14px 4px 0;min-height:150px}
.banner{height:581px}
.giveaway{top:2842px}
.banner .photo{height:252px}
.band{background:#3a3b3d;color:#fff;font-family:"Oswald",sans-serif;font-weight:600;font-size:32px;line-height:1.2;text-transform:uppercase;text-align:center;padding:14px 40px}
.cols{display:flex;gap:28px;padding:22px 40px;font-size:12.5px;line-height:1.5}
.cols p{flex:1}
.redeem{top:3458px;height:553px;display:flex;padding:18px}
.redeem .purple{width:400px;height:517px;flex:none}
.redeem .txt{padding:8px 8px 0 30px;font-size:12.5px}
.redeem .txt p{margin-top:12px}
.support{top:4046px;height:380px;display:flex;padding:24px 30px}
.support .txt{flex:1;font-size:12.5px;padding-right:30px}
.support .txt p{margin-top:12px}
.support .purple{width:380px;height:300px;flex:none;margin-top:20px}
.toogood{top:4461px;height:622px}
.toogood .photo{height:230px}
.footer{top:5118px;left:0;width:1200px;height:69px;display:flex;align-items:center;justify-content:space-between;padding:0 62px;font-size:11px;color:#999}
.footer span{color:var(--blue-bright)}
</style>
</head>
<body>

<div class="abs topbar"><span>☎ 800-555-0142</span><span>✉ hello@brightlanepromoworks.biz</span>
  <div class="login"><div class="field"></div><div class="field"></div><div class="btn">Login</div><div class="btn">Sign Up</div></div></div>

<header class="abs nav">
  <div class="brand"><i></i>Brightlane Promo Works</div>
  <ul><li class="on">HOME</li><li>OUR INCENTIVES</li><li>SAMPLES</li><li>HOW IT WORKS</li><li>TESTIMONIALS</li><li>FAQ</li><li>CONTACT</li></ul>
</header>

<section class="abs hero" role="img" aria-label="Tablet showing a hexagon-patterned promotional certificate app"></section>
<h1 class="abs hero-title">Brightlane Promo Works<br>Incentives</h1>
<div class="abs hero-facts">12 Years In Business<br>13,000+ Clients Enrolled<br>2+ Million Certificates In Circulation<br>170,000 + Redemptions To Date<br>A Rating With Trusted Commerce Bureau<br>Licensed Seller Of Travel CST #4817306</div>
<div class="abs hero-cta">RISK FREE FOR 30 DAYS <b>›</b></div>

<section class="abs card incentives">
  <h2 class="h2">Our Incentives</h2>
  <div class="inc-cols">
    <ul><li>• Airfare &amp; Hotel - U.S. ONLY</li><li>• 2 Night Resort</li><li>• 1-4 Night Las Vegas</li><li>• Luxurious Mexico Beach Resort</li><li>• Getaway Stay In Cabo San Lucas</li></ul>
    <ul><li>• 1 Night Hotel Stay</li><li>• 2 Night Hotel Stay</li><li>• 3 Night Hotel Stay</li><li>• 4 Night Hotel Stay</li><li>• 7 inch Wi-Fi Tablet</li></ul>
    <ul><li>• Touch Mp4 Player</li><li>• Mini Digital Camcorder</li><li>• New Premium Quality Earbuds</li><li>• Premium $25 Restaurant Gift</li><li>• $300 Restaurant Certificate</li></ul>
    <ul><li>• Premium $50 CB Gras</li><li>• Premium $50 CB Gas</li><li>• Premium $100 Cash Back Gas</li><li>• Premium $100 Cash Back Gras</li><li>• Free Healthcare Discount Card</li></ul>
  </div>
</section>

<section class="abs card feature">
  <div class="photo" role="img" aria-label="Monitor on a desk showing a climb to success graphic"></div>
  <div class="txt">
    <div class="sub">Increase leads and sales from your existing marketing efforts by offering high perceived value incentives to your customers!</div>
    <p>Create a variety giveaway promotions for your business with an unlimited supply of top quality vacation getaway certificates, restaurant gift certificates, electronic product giveaways and gas or grocery rewards for just $99/mth. Whether you need 100 or 100,000 you will never pay more than $99.</p>
  </div>
</section>

<section class="abs card plug">
  <h2 class="h2">We plug right into your existing<br>business model in 4 ways</h2>
  <div class="plug-grid">
    <div class="plug-item"><div class="icon-sq"><svg width="54" height="46" viewBox="0 0 54 46"><path d="M4 16h46l-6 26H10z" fill="#fff"/><path d="M16 16l8-14M38 16l-8-14" stroke="#fff" stroke-width="4"/></svg></div>
      <div><h3>Boost Response Rates To Your Existing Ads</h3><p>By adding one extra tagline: "Call for a Free Quote and receive a Three Day Two Night Hotel Stay Certificate to Las Vegas or 50 + other destinations, No Purchase Necessary." Imagine how many more leads you could generate.</p></div></div>
    <div class="plug-item"><div class="icon-sq"><svg width="40" height="54" viewBox="0 0 40 54"><path d="M2 2h36M2 52h36M6 2c0 18 28 18 28 25S6 34 6 52M34 2c0 18-28 18-28 25s28 7 28 25" stroke="#fff" stroke-width="4" fill="none"/></svg></div>
      <div><h3>Get More New Customers</h3><p>Now that you have generated a new lead, try enticing them with an upgrade and offer them Two Nights Plus Airfare if they purchase today.</p></div></div>
    <div class="plug-item"><div class="icon-sq"><svg width="50" height="46" viewBox="0 0 50 46"><path d="M2 2v42h46" stroke="#fff" stroke-width="4" fill="none"/><rect x="10" y="26" width="7" height="14" fill="#fff"/><rect x="22" y="16" width="7" height="24" fill="#fff"/><rect x="34" y="8" width="7" height="32" fill="#fff"/></svg></div>
      <div><h3>Increase Repeat &amp; Referral Business</h3><p>Reward past clients about your products &amp; services with a 7 Night Resort Getaway in one of over 3500 destinations around the world to motivate repeat business and to anyone who fulfills your request for a new referral.</p></div></div>
    <div class="plug-item"><div class="icon-sq"><svg width="56" height="44" viewBox="0 0 56 44"><circle cx="18" cy="12" r="9" fill="#fff"/><circle cx="40" cy="14" r="7" fill="#fff"/><path d="M2 44c0-14 8-20 16-20s16 6 16 20zM30 44c0-10 4-16 10-16s14 6 14 16z" fill="#fff"/></svg></div>
      <div><h3>Residual Business</h3><p>Remind past clients about your products &amp; services with a 2 Night Stay of your previous business clients using a personal touch and an incentive to boot.</p></div></div>
  </div>
</section>

<section class="abs card dist">
  <h2 class="h2">Easy Distribution</h2>
  <div class="dist-grid">
    <div class="tile"><div class="tile-ico"><svg width="110" height="96" viewBox="0 0 110 96"><rect x="26" y="2" width="58" height="30" fill="#2a8fe6"/><rect x="2" y="36" width="106" height="40" rx="6" fill="#2a8fe6"/><rect x="24" y="60" width="62" height="34" fill="#2a8fe6" stroke="#2b2c2e" stroke-width="4"/></svg></div><div class="tile-bar">Print</div>
      <p>Download PDF certificates to print and physically hand them out or mail them to your customers!</p></div>
    <div class="tile"><div class="tile-ico"><svg width="110" height="76" viewBox="0 0 110 76"><rect x="2" y="2" width="106" height="72" fill="#2a8fe6"/><path d="M4 6l51 40 51-40" stroke="#2b2c2e" stroke-width="5" fill="none"/></svg></div><div class="tile-bar">Mail</div>
      <p>Email e-certificates to your customers individually or in bulk with just one click!</p></div>
    <div class="tile"><div class="tile-ico"><svg width="100" height="100"><circle cx="50" cy="50" r="46" fill="#2a8fe6"/></svg></div><div class="tile-bar">Online Automation</div>
      <p>Add our web banners on your website. Your customers click on the banners to get their certificate, 100% automated! Use the banners to help increase lead generation conversion rates or give it as a thank you page after the customer purchases or completes another desired action, like opting in for a newsletter or webinar.</p></div>
    <div class="tile"><div class="tile-ico"><svg width="100" height="92" viewBox="0 0 100 92"><ellipse cx="50" cy="40" rx="46" ry="36" fill="#2a8fe6"/><path d="M22 64L12 90l34-18z" fill="#2a8fe6"/></svg></div><div class="tile-bar">SMS</div>
      <p>Send sms certificates through text messaging with just one click!</p></div>
  </div>
</section>

<section class="abs card banner giveaway">
  <div class="photo" role="img" aria-label="Climb to success graphic on a computer screen"></div>
  <div class="band">Give away an unlimited amount of certificates to your<br>customers for just $99 bucks a month</div>
  <div class="cols">
    <p>We are A rated with the Trusted Commerce Bureau as well as a licensed seller of travel registered with the state Attorney General's office (CST #4817306). We are also participants in the Traveler Protection Fund (TPF), which was created to protect consumers from unscrupulous travel companies. TPF is a program that requires</p>
    <p>travel agencies like us to build a "Passenger Trust Account" and requires that all traveler funds that we collect must be deposited into this account. If a consumer contacts the Attorney General to complain about us and our associates, they have 100% access to the "Passenger Trust Account" and has the right to take money from the account</p>
    <p>to give back to the dissatisfied consumer. So every consumer that deals with our business is protected specifically under this program that we are a member of.</p>
  </div>
</section>

<section class="abs card redeem">
  <div class="purple" role="img" aria-label="Tablet showing the certificate redemption system"></div>
  <div class="txt">
    <div class="sub">Completely separate redemption websites - online redemption - online reservation requests</div>
    <p>First and foremost we're a marketing company and we will protect the integrity of your promotions. By using separate redemption websites keeps your customers from finding out what a great value you are getting. We offer by far what is known as the most end-user friendly redemption process in the industry. Most of your customers will redeem their certificate on one of our redemption websites and they won't have to wait for a "reservation request form" in the mail.</p>
    <p>Our redemption websites also feature 24/7 status reporting. Your customers will be able to log in to the redemption website with their original certificate code for up to 6 months after they redeem their certificate to check on their status or even reprint their reservation confirmation. First and foremost we're a marketing company and we will protect the integrity of your promotions. By using separate redemption websites keeps your customers from finding out what a great value you are getting.</p>
    <p>Most of your customers will redeem their certificate on one of our redemption websites and they won't have to wait for a "reservation request form" in the mail. With us, your customers can fill out their reservation request form right online immediately after redemption! Our redemption websites also feature 24/7 status reporting. Your customers will be able to log in to the redemption website with their original certificate code for up to 6 months after they redeem their certificate to check on their status or to even reprint their reservation confirmation.</p>
  </div>
</section>

<section class="abs card support">
  <div class="txt">
    <div class="sub">Top notch customer service with superior member support</div>
    <p>We are easy to contact and we always answer our phone during business hours. We even have a 24-hour live answering service that takes out calls just to guarantee that we never miss a call after hours or if we happen to be busy on the other lines. As a member, one of our Senior Incentive Marketing Consultants will create a custom incentive marketing plan specific for your company at your request for no additional cost. We have also created the easiest redemption process in the industry so you do not have to worry about your customers receiving their gift.</p>
    <p>We facilitate your customers all the way from redemption to fulfillment. Remember, we are the manufacturer of our offers and we currently fulfill all of our travel certificates in-house. With our support ticket systems, our 800 #s, online contact us forms, and our 24/7 online redemption status websites, you and your customers will never have any problems getting in contact with us. Since there are no long term contracts with our service, we are forced to prove ourselves to you month in and month out.</p>
  </div>
  <div class="purple" role="img" aria-label="Tablet with hexagon-patterned support dashboard"></div>
</section>

<section class="abs card banner toogood">
  <div class="photo" role="img" aria-label="Travelers relaxing at a resort destination"></div>
  <div class="band">Too good to be true! How do we do it?</div>
  <div class="cols">
    <p>Brightlane Promo Works Group Inc. contracts with the world leading hotel chains and resorts to help fill their otherwise empty rooms when they need it most. We help fill empty rooms which the properties turn into future sales. Hotels rarely experience full occupancy, yet they remain open and they still have their fixed costs. So when the properties give out their rooms by partnering with us, they might miss out on the room fee, remember</p>
    <p>the room was empty anyways, but now they gain a customer in their in-house restaurants, room service, the casino, spa and other amenities within their property. They're (the hotels and resorts) are doing it for the same reason why you would be using these incentives; to increase your repeat and referral business. They know that if they show your customers a good time on their vacation they'll be more likely to tell their friends and family about the</p>
    <p>great time they had and hopefully will come back to stay there at a regular rate in the future. Since we contract with the largest travel conglomerates in the travel industry today, this ensures top quality vacations for your customers with No Timeshare Or Sales Presentations, Guaranteed! In fact, we won't work with any property that has less than a 3-star rating by other travelers from www.TravelReviewHub.com.</p>
  </div>
</section>

<footer class="abs footer"><div>© 2000-2018 Brightlane Promo Works Group Inc. - All Rights Reserved</div><div><span>Affiliate Program</span> | <span>Terms &amp; Conditions</span> | <span>Privacy Policy</span> | <span>Login</span></div></footer>

</body>
</html>
```